Postcard design to acquire new clients for my Property Management Company

I'm looking for a postcard design that I can send to prospective clients detailing information about my company and services.
Postcard should be eye catching and contain information from www.brightkeyrentals-example.com. I've provided a few screen shots for the most important information and my logo.
Target Market(s)
Real Estate
Industry/Entity Type
Real Estate
Font styles to use
Sans Serif
Requirements
Must have
- Must be eye catching!! this will be a direct mail piece - I'd like for the card to be read and not tossed in the trash immediately.
Design que from the logo.
A place to write / print the receipts name and address.
our physical address - 2287 Marble Lane, Lubbock, TX 79555.
Should not have
- the contact information on the business card is not accurate - please use info from website.

```html
<!DOCTYPE html>
<html lang="en">
<head>
<meta charset="UTF-8">
<title>BrightKey Rentals – Direct Mail Postcard</title>
<link href="https://fonts.googleapis.com/css2?family=Montserrat:wght@400;500;600;700;800&display=swap" rel="stylesheet">
<style>
  :root{
    --stage:#1b1b1c;
    --brand-blue:#1d538b;
    --panel-gray:#9b9b9b;
    --ink:#161616;
    --paper:#ffffff;
    --rule:#222222;
  }
  *{box-sizing:border-box;margin:0;padding:0}
  html,body{width:1200px;height:564px;overflow:hidden}
  body{background:var(--stage);font-family:'Montserrat',Arial,sans-serif;position:relative}

  .card{position:absolute;width:522px;height:348px;overflow:hidden;background:var(--paper)}
  .card--front{left:51px;top:104px}
  .card--back{left:623px;top:104px}

  /* front */
  .front-art{position:absolute;inset:0}
  .brand{position:absolute;left:10px;color:var(--brand-blue);font-weight:700;line-height:1;white-space:nowrap}
  .brand__name{top:26px;font-size:22px;letter-spacing:4px}
  .brand__sub{top:52px;font-size:10.5px;letter-spacing:3.2px}
  .headline-line{position:absolute;left:5px;line-height:1;white-space:nowrap}
  .headline__main{top:122px;font-size:44px;font-weight:800;color:var(--ink);letter-spacing:-0.5px}
  .headline__second{top:167px;font-size:30px;font-weight:700;color:var(--ink)}
  .headline__place{top:200px;font-size:23px;font-weight:600;color:var(--paper)}
  .accent-rule{position:absolute;left:0;top:240px;width:44px;height:2px;background:var(--brand-blue)}
  .tagline{position:absolute;left:4px;top:255px;font-size:12.5px;font-weight:500;color:var(--paper);line-height:1.25}
  .contact-bar{position:absolute;left:0;top:306px;width:522px;height:42px}
  .contact-bar__label{position:absolute;left:0;top:0;width:138px;height:42px;background:var(--panel-gray);color:var(--ink);font-weight:800;font-size:17px;line-height:42px;padding-left:10px}
  .contact-bar__items{position:absolute;left:138px;top:0;width:384px;height:42px;background:var(--brand-blue);color:var(--paper)}
  .contact-item{position:absolute;top:0;height:42px;display:flex;align-items:center;gap:6px;font-weight:500;white-space:nowrap}
  .contact-item--phone{left:18px;font-size:13px}
  .contact-item--email{left:146px;font-size:10.5px}
  .contact-item svg{fill:var(--paper);flex:none}

  /* back */
  .services{position:absolute;left:0;top:0;width:311px;height:273px;background:var(--panel-gray)}
  .services__title{position:absolute;left:0;top:8px;width:311px;height:21px;background:var(--brand-blue);color:var(--paper);font-weight:800;font-size:15px;text-align:center;line-height:21px}
  .service{position:absolute}
  .service--left{left:35px;width:112px}
  .service--right{left:180px;width:118px}
  .service__icon{position:absolute;left:-27px;top:-3px;width:21px;height:21px;fill:var(--brand-blue)}
  .service__name{color:var(--brand-blue);font-weight:600;font-size:10.5px;line-height:1.2;white-space:nowrap}
  .service__text{color:var(--ink);font-size:6.8px;line-height:1.05;margin-top:3px;font-weight:500}
  .closing{position:absolute;left:0;top:273px;width:311px;height:75px;background:var(--brand-blue);color:var(--paper);font-weight:700;font-size:15.5px;text-align:center;line-height:1.25;padding-top:13px}
  .mailing{position:absolute;left:311px;top:0;width:211px;height:348px;background:var(--paper)}
  .stamp-box{position:absolute;left:124px;top:8px;width:75px;height:80px;border:1.5px solid var(--rule)}
  .return-address{position:absolute;left:19px;top:100px;font-size:7.5px;color:var(--ink);font-weight:500}
  .address-line{position:absolute;left:19px;width:180px;height:1px;background:var(--rule)}
</style>
</head>
<body>

<section class="card card--front" aria-label="Postcard front">
  <svg class="front-art" width="522" height="348" viewBox="0 0 522 348">
    <defs>
      <linearGradient id="sceneTones" x1="0" y1="0" x2="0" y2="1">
        <stop offset="0" stop-color="#3b66b8"/>
        <stop offset="0.35" stop-color="#9fb6d6"/>
        <stop offset="0.6" stop-color="#e6e8ea"/>
        <stop offset="0.85" stop-color="#8a7460"/>
        <stop offset="1" stop-color="#4d90c4"/>
      </linearGradient>
    </defs>
    <rect width="522" height="348" fill="#ffffff"/>
    <polygon points="0,82 192,82 224,50 371,306 0,306" fill="#9b9b9b"/>
    <polygon points="199,0 522,0 522,306 380,306 230,52" fill="url(#sceneTones)" role="img" aria-label="Photo of a white two-storey beach house with wraparound porches, red lounge chairs and a pool"/>
  </svg>

  <div class="brand brand__name">BRIGHTKEY</div>
  <div class="brand brand__sub">RENTALS</div>

  <h1>
    <span class="headline-line headline__main">PROPERTY</span>
    <span class="headline-line headline__second">MANAGEMENT</span>
    <span class="headline-line headline__place">ACROSS LUBBOCK</span>
  </h1>
  <div class="accent-rule"></div>
  <p class="tagline">Maximize your financial returns with<br>support from our rental specialists</p>

  <div class="contact-bar">
    <div class="contact-bar__label">Get In Touch</div>
    <div class="contact-bar__items">
      <span class="contact-item contact-item--phone">
        <svg width="15" height="15" viewBox="0 0 24 24"><path d="M6.6 10.8a15.1 15.1 0 0 0 6.6 6.6l2.2-2.2a1 1 0 0 1 1-.25 11.4 11.4 0 0 0 3.6.57 1 1 0 0 1 1 1V20a1 1 0 0 1-1 1A17 17 0 0 1 3 4a1 1 0 0 1 1-1h3.5a1 1 0 0 1 1 1c0 1.25.2 2.45.57 3.57a1 1 0 0 1-.25 1z"/></svg>
        (806) 555-0147
      </span>
      <span class="contact-item contact-item--email">
        <svg width="17" height="12" viewBox="0 0 24 16"><path d="M0 0h24v16H0z" fill="none" stroke="#fff" stroke-width="2"/><path d="M1 1l11 8 11-8" fill="none" stroke="#fff" stroke-width="2"/></svg>
        info@brightkeyrentals-example.com
      </span>
    </div>
  </div>
</section>

<section class="card card--back" aria-label="Postcard back">
  <div class="services">
    <h2 class="services__title">OUR SERVICES</h2>

    <div class="service service--left" style="top:44px">
      <svg class="service__icon" viewBox="0 0 24 24"><path d="M12 3 1 12h3v9h6v-6h4v6h6v-9h3z"/></svg>
      <div class="service__name">Property Marketing</div>
      <p class="service__text">Let us take over your marketing for you and we'll find a qualified renter quickly.</p>
    </div>
    <div class="service service--left" style="top:94px">
      <svg class="service__icon" viewBox="0 0 24 24"><circle cx="8" cy="7" r="4"/><circle cx="17" cy="8" r="3"/><path d="M0 20c0-5 3-7 8-7s8 2 8 7zM15 13c5 0 9 2 9 7h-6c0-3-1-5-3-7z"/></svg>
      <div class="service__name">Tenant Screening</div>
      <p class="service__text">We don't just find someone to rent your home—we find the best renters. We screen all applications using fair housing guidelines to protect you.</p>
    </div>
    <div class="service service--left" style="top:150px">
      <svg class="service__icon" viewBox="0 0 24 24"><text x="6" y="21" font-size="22" font-weight="700" font-family="Montserrat, sans-serif" fill="#1d538b">$</text></svg>
      <div class="service__name">Rent Collection</div>
      <p class="service__text">Stop guessing when you'll receive your rental earnings every month and say hello to consistent payments. We keep your tenants current.</p>
    </div>
    <div class="service service--left" style="top:208px">
      <svg class="service__icon" viewBox="0 0 24 24"><path d="M13 2l9 7-3 3-3-2-11 12-3-3 12-11-2-3z"/></svg>
      <div class="service__name">Maintenance</div>
      <p class="service__text">Still scrambling to respond to repair requests every time you receive a tenant call? Let us coordinate repair work on your behalf!</p>
    </div>

    <div class="service service--right" style="top:43px">
      <svg class="service__icon" viewBox="0 0 24 24"><circle cx="10" cy="10" r="7" fill="none" stroke="#1d538b" stroke-width="3"/><path d="M15 15l7 7" stroke="#1d538b" stroke-width="3.5"/></svg>
      <div class="service__name">Property Inspections</div>
      <p class="service__text">We visit every home in our portfolio regularly.</p>
    </div>
    <div class="service service--right" style="top:85px">
      <svg class="service__icon" viewBox="0 0 24 24"><path d="M2 2v20h20v-2H4V2z"/><rect x="7" y="12" width="2" height="6"/><rect x="11" y="8" width="2" height="10"/><rect x="15" y="10" width="2" height="8"/><rect x="19" y="5" width="2" height="13"/></svg>
      <div class="service__name">Financial Reporting</div>
      <p class="service__text">Keep a handle on your real estate performance. We generate monthly statements so you can review income &amp; expenses at a moment's notice.</p>
    </div>
    <div class="service service--right" style="top:145px">
      <svg class="service__icon" viewBox="0 0 24 24"><path d="M12 1 3 5v6c0 6 4 10 9 12 5-2 9-6 9-12V5zm0 3v16c-3-1.5-6-4.5-6-9V7z"/></svg>
      <div class="service__name">Evictions</div>
      <p class="service__text">When things go wrong inside your rental home, rest easy with the experts on your side. We will handle evictions for you &amp; find new renters when its over.</p>
    </div>
    <div class="service service--right" style="top:206px">
      <svg class="service__icon" viewBox="0 0 24 24"><path d="M11 3h2v17h5v2H6v-2h5z"/><path d="M3 6h18v1.5H3z"/><path d="M5 7 1.5 14h7zM19 7l-3.5 7h7z" fill="none" stroke="#1d538b" stroke-width="1.6"/><path d="M1.5 14a3.5 2 0 0 0 7 0zM15.5 14a3.5 2 0 0 0 7 0z"/></svg>
      <div class="service__name">Legal Guidance</div>
      <p class="service__text">Don't accidentally violate one of the many ordinances and housing laws governing your relationship with your tenants. Let us keep you compliant.</p>
    </div>
  </div>

  <h2 class="closing">CHOOSE THE RIGHT<br>PROPERTY MANAGEMENT SYSTEM</h2>

  <div class="mailing">
    <div class="stamp-box" aria-label="Stamp area"></div>
    <p class="return-address">2287 Marble Lane, Lubbock, TX 79555</p>
    <div class="address-line" style="top:127px"></div>
    <div class="address-line" style="top:177px"></div>
    <div class="address-line" style="top:228px"></div>
  </div>
</section>

</body>
</html>
```